Meridian Rest Supply Needs Business Card

Looking for a very nice looking business card. Creative but not extravagant. We sell beds and pillows across the U.S. and need something professional but catchy. I have attached the logo.

Name : Dale Fenwick
Title : President
Phone : (800) 417-2964
Email: sleep@quorvana.com
Website: www.quorvana.com

Can be single-sided or double-sided
horizontal or vertical

Can use Blues/Greys

Target Market(s)

Mass Market

Industry/Entity Type

Retail

Contact Information for Business Card

Name : Dale Fenwick
Title : President
Phone : (800) 417-2964
Email: sleep@quorvana.com
Website: www.quorvana.com

Requirements
Must have
• Clean, Modern, Smooth
• Can use Blues/Greys
• On the other side without the information - have something simple like www.quorvana.com or our logo
Nice to have
• Surprise me
Should not have
• Nothing crazy, nothing cluttered

```html
<!DOCTYPE html>
<html lang="en">
<head>
<meta charset="utf-8">
<title>Quorvana Business Card</title>
<link rel="stylesheet" href="https://fonts.googleapis.com/css2?family=Quicksand:wght@300;400&family=Roboto+Condensed:wght@400&display=swap">
<style>
  :root {
    --page-bg: #151617;
    --card-center: #0f3d44;
    --card-edge: #072125;
    --frame-line: rgba(120, 190, 200, 0.16);
    --accent-blue: #3ba9dc;
    --text-white: #f2f5f6;
  }
  * { margin: 0; padding: 0; box-sizing: border-box; }
  html, body {
    width: 1200px;
    height: 1200px;
    overflow: hidden;
    background: var(--page-bg);
  }
  .sheet {
    width: 1200px;
    height: 1200px;
    display: flex;
    flex-direction: column;
    align-items: center;
    justify-content: center;
    gap: 70px;
  }
  .card {
    position: relative;
    width: 700px;
    height: 400px;
    background: radial-gradient(ellipse at 50% 45%, var(--card-center) 0%, var(--card-edge) 100%);
    box-shadow: 0 18px 40px rgba(0, 0, 0, 0.55);
  }
  .card-frame {
    position: absolute;
    inset: 18px;
    border: 1px solid var(--frame-line);
  }
  .card-front {
    display: flex;
    align-items: center;
    justify-content: center;
  }
  .brand-name {
    font-family: "Roboto Condensed", sans-serif;
    font-weight: 400;
    font-size: 52px;
    letter-spacing: 1px;
    color: var(--text-white);
  }
  .holder {
    position: absolute;
    right: 400px;
    top: 128px;
    text-align: right;
    font-family: "Quicksand", sans-serif;
    font-weight: 400;
    color: var(--text-white);
  }
  .holder-name {
    font-size: 30px;
    letter-spacing: 0.5px;
    line-height: 1.1;
  }
  .holder-title {
    font-size: 19px;
    font-weight: 300;
    letter-spacing: 0.5px;
    margin-top: 4px;
  }
  .divider {
    position: absolute;
    left: 318px;
    top: 118px;
    width: 1px;
    height: 150px;
    background: var(--frame-line);
  }
  .contact-list {
    position: absolute;
    left: 340px;
    top: 200px;
    list-style: none;
    font-family: "Roboto Condensed", sans-serif;
    font-size: 22px;
    line-height: 1.28;
  }
  .contact-label { color: var(--accent-blue); }
  .contact-value { color: var(--text-white); }
</style>
</head>
<body>
  <main class="sheet">
    <section class="card card-front">
      <div class="card-frame"></div>
      <span class="brand-name">Quorvana</span>
    </section>

    <section class="card card-back">
      <div class="card-frame"></div>
      <div class="holder">
        <p class="holder-name">DALE FENWICK</p>
        <p class="holder-title">PRESIDENT</p>
      </div>
      <div class="divider"></div>
      <ul class="contact-list">
        <li><span class="contact-label">Phone : </span><span class="contact-value">(800) 417-2964</span></li>
        <li><span class="contact-label">Email : </span><span class="contact-value">sleep@quorvana.com</span></li>
        <li><span class="contact-label">Website : </span><span class="contact-value">www.quorvana.com</span></li>
      </ul>
    </section>
  </main>
</body>
</html>
```